Volunteer Marketplace Needs New Look - www.Mipsko.org

Mipsko is the first online marketplace that lets you buy or sell volunteered services to raise money for charity. (www.Mipsko.org)

We went into live testing a few months ago to get some feedback and feel we need to redo the design. Some points:

- The current design was developed when a previous logo was being used. We later developed the current logo (which we love) and have never felt it really fit into the design. A design that plays up the logo would be great but not required.

- The circles in the logo represent coins which is a theme we are using in our branding (our business cards are coins). The marketplace offers a new form of currency people can use to give back. We don't feel the design should center around this concept, but a small element would be a nice touch.

We want a design that is engaging and fun - but still professional and credible.
Updates

I just want to thank you all for submitting designs. I have been trying to send feedback to everyone and am starting to eliminate designs so I can begin to narrow it. It is so hard to decide. You all did a great job! 

Target Market(s)

There are three target audiences - volunteers donating their services, customers buying donated services, and charities joining the program.

Industry/Entity Type

Business

Requirements
Must have
• - We feel we need to represent on the home page the concept of there being two parties that are coming together - the Volunteer and the Customer.

- We have a 60 second overview video in the works that we would like displayed on the home page.
Nice to have
• Incase it is helpful, here are some designs we like - but please know we are looking for creative ideas. Your design does not have to look like these.

http://www.lendora-sample.org/
https://www.wexaro.com/
http://www.layoutbarn.com/website-templates/40056.html
http://www.layoutbarn.com/website-templates/40121.html
http://www.pixelhive.com/

Also - please be creative about what content we put on our home page. We want to modernize the site. We can feed in our blog, twitter, facebook, etc into the home page if you think we should. We need your expertise to recommend what we need to showcase.
Should not have
• Please note that the paragraphs of content do not have to be on the home page. These are there now, but feedback tells us it is too boring - and they is why we are having the video done. So - you do not have to make room for all that text.

```html
<!DOCTYPE html>
<html lang="en">
<head>
<meta charset="utf-8">
<title>Mipsko</title>
<link rel="stylesheet" href="https://fonts.googleapis.com/css2?family=Arimo:wght@400;700&display=swap">
<style>
:root{
  --ink:#333333;
  --ink-soft:#555555;
  --page:#e6e6e6;
  --white:#ffffff;
  --green-top:#8fcf3a;
  --green-bottom:#6cb52a;
  --yellow:#ffd21a;
  --yellow-dark:#e7b200;
  --orange:#ff5a14;
  --gold:#f6c400;
  --cyan:#1cb3d6;
  --row-alt:#eeeeee;
  --win:#777777;
  --footer-bottom:#2b2b2b;
}
*{box-sizing:border-box;margin:0;padding:0}
html,body{width:1050px;height:1200px;overflow:hidden}
body{position:relative;background:var(--page);font-family:"Arimo",Arial,sans-serif;color:var(--ink)}
.abs{position:absolute}

/* header */
.site-header{left:0;top:0;width:1050px;height:108px;background:linear-gradient(#ffffff 0%,#f4f4f4 55%,#d9d9d9 100%);border-bottom:6px solid var(--white)}
.brand-name{left:165px;top:26px;font-size:46px;font-weight:700;color:var(--ink-soft);line-height:1}
.account{left:745px;top:13px;display:flex;gap:5px}
.account a{display:block;width:64px;height:23px;border:1px solid #c9c9c9;border-radius:12px;background:linear-gradient(#ffffff,#e3e3e3);font-size:11px;text-align:center;line-height:21px;color:var(--ink);text-decoration:none}
.main-nav{left:552px;top:75px;display:flex;gap:15px}
.main-nav a{display:block;height:32px;border:1px solid #cfcfcf;border-bottom:none;border-radius:5px 5px 0 0;background:linear-gradient(#ffffff,#ececec);font-size:11.5px;font-weight:700;color:var(--ink);text-decoration:none;text-align:center;line-height:32px}
.main-nav a.active{background:#ffffff}

/* hero */
.hero{left:0;top:114px;width:1050px;height:322px;background:linear-gradient(var(--green-top),var(--green-bottom));box-shadow:0 10px 18px rgba(0,0,0,.18)}
.video{left:165px;top:140px;width:336px;height:276px;background:#000;border:1px solid #6a6a6a}
.video-spinner{left:157px;top:116px}
.video-controls{left:0;bottom:0;width:334px;height:23px}
.people{left:537px;top:137px;width:353px;height:210px;display:grid;grid-template-columns:repeat(5,68px);grid-template-rows:repeat(3,67px);gap:3px}
.people span{display:block;border:2px solid #ffffff;background:linear-gradient(#d8d2c8,#b8ab9c)}
.people span:nth-child(5n+3){background:linear-gradient(#9a9a9a,#5e5e5e)}
.people span:nth-child(5n+4){background:linear-gradient(#c9c1a6,#8f7e64)}
.people span:nth-child(5n+5){background:linear-gradient(#d7e0d6,#c7b08e)}
.cta{top:369px;width:170px;height:47px;border:1px solid #d19d00;border-radius:3px;background:linear-gradient(#ffe24a,var(--yellow) 50%,var(--yellow-dark));color:#6a4a00;font-size:14px;font-weight:700;text-align:center;line-height:17px;padding-top:7px;text-decoration:none}
.cta-hire{left:537px}
.cta-volunteer{left:720px}

/* intro */
.motto{left:0;top:462px;width:1050px;text-align:center;font-size:25px;font-weight:700;color:#505050}
.step{top:519px;width:236px;height:164px;background:#ffffff;border:1px solid #d6d6d6;border-radius:6px 6px 22px 22px;box-shadow:0 3px 5px rgba(0,0,0,.12)}
.step h3{height:37px;border-bottom:1px solid #dcdcdc;background:linear-gradient(#fafafa,#efefef);border-radius:6px 6px 0 0;font-size:14px;font-weight:700;text-align:center;line-height:37px;color:var(--ink)}
.step-icon{left:11px;top:64px;width:60px;height:60px;border-radius:4px;display:flex;align-items:center;justify-content:center}
.step p{left:83px;top:62px;width:145px;font-size:11px;line-height:14px;color:var(--ink-soft)}
.step-hire{left:155px}.step-hire .step-icon{background:var(--orange)}
.step-manage{left:407px}.step-manage .step-icon{background:var(--gold)}
.step-pay{left:660px}.step-pay .step-icon{background:var(--cyan)}
.dollar{font-size:44px;font-weight:700;color:#fff;line-height:1}

/* projects */
.section-title{top:712px;font-size:17px;font-weight:700;color:var(--ink)}
.projects{top:744px;width:378px;height:266px;background:#fff;border:1px solid #cfcfcf;border-radius:5px;box-shadow:0 2px 4px rgba(0,0,0,.1)}
.projects table{position:absolute;left:6px;top:14px;width:364px;border-collapse:collapse;font-size:11px}
.projects th{height:30px;font-weight:700;text-align:center;color:var(--ink)}
.projects td{height:34px;text-align:center;color:#444444}
.projects tbody tr:nth-child(odd){background:var(--row-alt)}
.projects th:first-child,.projects td:first-child{text-align:left;padding-left:24px;width:200px}
.win{display:inline-block;width:24px;height:24px;background:var(--win);vertical-align:middle}
.more{top:1026px;width:378px;height:36px;border:1px solid #c9c9c9;border-radius:4px;background:linear-gradient(#f7f7f7,#dcdcdc);font-size:11px;font-weight:700;color:var(--ink);text-align:center;line-height:34px;text-decoration:none}

/* footer */
.site-footer{left:0;top:1076px;width:1050px;height:124px;background:linear-gradient(#2e2e2e,#4a4a4a 55%,#3a3a3a)}
.footer-links{left:0;width:1050px;text-align:center;font-size:11px;color:#fff}
.footer-links span{margin:0 6px;color:#cfcfcf}
.copyright{left:0;top:1167px;width:1050px;height:33px;background:var(--footer-bottom);color:#fff;font-size:11px;text-align:center;line-height:33px}
</style>
</head>
<body>

<header class="site-header abs">
  <div class="brand-name abs">Mipsko</div>
  <nav class="account abs"><a href="#">Login</a><a href="#">Sign Up</a></nav>
  <nav class="main-nav abs">
    <a href="#" class="active" style="width:105px">Hire The Talent</a>
    <a href="#" style="width:105px">Find The Projects</a>
    <a href="#" style="width:113px">How It Works</a>
  </nav>
</header>

<section class="hero abs"></section>

<div class="video abs" role="img" aria-label="Overview video player">
  <svg class="video-spinner abs" width="20" height="20" viewBox="0 0 20 20">
    <g fill="#bbb">
      <circle cx="10" cy="2.5" r="1.8"/><circle cx="15.3" cy="4.7" r="1.6" opacity=".9"/>
      <circle cx="17.5" cy="10" r="1.5" opacity=".8"/><circle cx="15.3" cy="15.3" r="1.4" opacity=".7"/>
      <circle cx="10" cy="17.5" r="1.3" opacity=".6"/><circle cx="4.7" cy="15.3" r="1.2" opacity=".5"/>
      <circle cx="2.5" cy="10" r="1.1" opacity=".4"/><circle cx="4.7" cy="4.7" r="1" opacity=".3"/>
    </g>
  </svg>
  <svg class="video-controls abs" width="334" height="23" viewBox="0 0 334 23">
    <defs><linearGradient id="ctrl" x1="0" y1="0" x2="0" y2="1"><stop offset="0" stop-color="#e6e6e6"/><stop offset="1" stop-color="#a5a5a5"/></linearGradient></defs>
    <rect x="0" y="0" width="334" height="23" fill="url(#ctrl)"/>
    <rect x="6" y="7" width="3" height="9" fill="#444"/><rect x="11" y="7" width="3" height="9" fill="#444"/>
    <rect x="22" y="7" width="2" height="9" fill="#444"/><path d="M32 7 L25 11.5 L32 16Z" fill="#444"/>
    <rect x="38" y="10" width="118" height="3" rx="1.5" fill="#666"/><circle cx="42" cy="11.5" r="4" fill="#eee" stroke="#555"/>
    <rect x="162" y="5" width="46" height="13" rx="2" fill="#222"/>
    <text x="185" y="14.5" font-size="7.5" fill="#ddd" text-anchor="middle" font-family="Arimo,Arial,sans-serif">00:00 / 01:47</text>
    <rect x="226" y="10" width="32" height="3" fill="#666"/><path d="M263 9 h3 l4 -3 v11 l-4 -3 h-3z" fill="#444"/>
    <rect x="295" y="7" width="12" height="9" fill="none" stroke="#444" stroke-width="1.5"/>
    <rect x="312" y="7" width="14" height="9" fill="none" stroke="#444" stroke-width="1.5"/>
  </svg>
</div>

<div class="people abs" role="img" aria-label="Grid of portrait photos of volunteers and customers">
  <span></span><span></span><span></span><span></span><span></span>
  <span></span><span></span><span></span><span></span><span></span>
  <span></span><span></span><span></span><span></span><span></span>
</div>

<a href="#" class="cta cta-hire abs">I Want To Hire<br>Donated Talent</a>
<a href="#" class="cta cta-volunteer abs">I Want To Volunteer<br>My Talents</a>

<h2 class="motto abs">“ The Place For The Talents For Charity To Doing A Project”</h2>

<article class="step step-hire abs">
  <h3>Hire The Talent</h3>
  <div class="step-icon abs">
    <svg width="30" height="32" viewBox="0 0 30 32"><circle cx="15" cy="10" r="7" fill="none" stroke="#fff" stroke-width="3"/><path d="M3 29 C3 20 27 20 27 29 Z" fill="none" stroke="#fff" stroke-width="3"/></svg>
  </div>
  <p class="abs">Lorem ipsum dolor sit amet, consecteteur adipiscing elit set diem nonumy.<br>In gravida neque, lorem ipsu m...</p>
</article>
<article class="step step-manage abs">
  <h3>Manage The Project</h3>
  <div class="step-icon abs">
    <svg width="34" height="36" viewBox="0 0 34 36"><rect x="5" y="3" width="24" height="30" fill="#fff" stroke="#9a7a00" stroke-width="1"/><g stroke="#777" stroke-width="2"><line x1="9" y1="10" x2="25" y2="10"/><line x1="9" y1="15" x2="25" y2="15"/><line x1="9" y1="20" x2="25" y2="20"/><line x1="9" y1="25" x2="20" y2="25"/></g></svg>
  </div>
  <p class="abs">Lorem ipsum dolor sit amet, consecteteur adipiscing elit set diem nonumy.<br>In gravida neque, lorem ipsu m...</p>
</article>
<article class="step step-pay abs">
  <h3>Pay After Done</h3>
  <div class="step-icon abs"><span class="dollar">$</span></div>
  <p class="abs">Lorem ipsum dolor sit amet, consecteteur adipiscing elit set diem nonumy.<br>In gravida neque, lorem ipsu m...</p>
</article>

<h2 class="section-title abs" style="left:145px">COMPLETED PROJECTS</h2>
<h2 class="section-title abs" style="left:541px">OPEN PROJECTS</h2>

<section class="projects abs" style="left:141px">
  <table>
    <thead><tr><th>Project Tittle</th><th>Budget</th><th>Talents</th><th>Win</th></tr></thead>
    <tbody>
      <tr><td>Lorem ipsum dolor sit amet</td><td>$300</td><td>10</td><td><span class="win"></span></td></tr>
      <tr><td>Lorem ipsum dolor sit amet</td><td>$300</td><td>10</td><td><span class="win"></span></td></tr>
      <tr><td>Lorem ipsum dolor sit amet</td><td>$300</td><td>10</td><td><span class="win"></span></td></tr>
      <tr><td>Lorem ipsum dolor sit amet</td><td>$300</td><td>10</td><td><span class="win"></span></td></tr>
      <tr><td>Lorem ipsum dolor sit amet</td><td>$300</td><td>10</td><td><span class="win"></span></td></tr>
      <tr><td>Lorem ipsum dolor sit amet</td><td>$300</td><td>10</td><td><span class="win"></span></td></tr>
    </tbody>
  </table>
</section>
<section class="projects abs" style="left:532px">
  <table>
    <thead><tr><th>Project Tittle</th><th>Budget</th><th>Talents</th><th>Win</th></tr></thead>
    <tbody>
      <tr><td>Lorem ipsum dolor sit amet</td><td>$300</td><td>10</td><td><span class="win"></span></td></tr>
      <tr><td>Lorem ipsum dolor sit amet</td><td>$300</td><td>10</td><td><span class="win"></span></td></tr>
      <tr><td>Lorem ipsum dolor sit amet</td><td>$300</td><td>10</td><td><span class="win"></span></td></tr>
      <tr><td>Lorem ipsum dolor sit amet</td><td>$300</td><td>10</td><td><span class="win"></span></td></tr>
      <tr><td>Lorem ipsum dolor sit amet</td><td>$300</td><td>10</td><td><span class="win"></span></td></tr>
      <tr><td>Lorem ipsum dolor sit amet</td><td>$300</td><td>10</td><td><span class="win"></span></td></tr>
    </tbody>
  </table>
</section>

<a href="#" class="more abs" style="left:141px">VIEW MORE COMPLETED PROJECTS</a>
<a href="#" class="more abs" style="left:532px">VIEW MORE OPEN PROJECTS</a>

<footer class="site-footer abs"></footer>
<nav class="footer-links abs" style="top:1082px">
  Home<span>I</span>Newsroom<span>I</span>About Mipsko<span>I</span>Charities<span>I</span>FAQ<span>I</span>Contact Mipsko<span>I</span>Terms &amp; Conditions<span>I</span>Privacy Policy<span>I</span>Blog<span>I</span>Sitemap
</nav>
<nav class="footer-links abs" style="top:1103px">
  Volunteer Opportunity<span>I</span>Volunteering Programs<span>I</span>Local Volunteer Program<span>I</span>Local Volunteer Work<span>I</span>Local Volunteering
</nav>
<div class="copyright abs">Copyright © 2012 mipsko, inc. All rights reserved. Mipsko is registered trademark of mipsko, inc. Patent Pending.</div>

</body>
</html>
```